Dwellcraft Brochure

We need a brochure on A4 to show our portfolio and invite people to take up our service offering. This brochure will be mailed to peoples home in the areas that we are targeting. We offer quick house modifications including bathroom and kitchen renovations, disability access, security, extensions and full house renovations as well as design and build services.

Target Market(s)

Home Owners, Occupational Therapists, Retirement village, Medical Centers

Industry/Entity Type

Construction and Design

Requirements
Must have
• Photos and our services listed and an invitation to use them

```html
<!DOCTYPE html>
<html lang="en">
<head>
<meta charset="utf-8">
<title>Dwellcraft Brochure</title>
<link href="https://fonts.googleapis.com/css2?family=Poppins:wght@400;500;600;700;800&display=swap" rel="stylesheet">
<style>
  :root {
    --red: #c4070d;
    --red-deep: #a8050a;
    --ink: #3d3d3d;
    --grey: #4a4a4a;
    --paper: #ffffff;
    --backdrop: #e9e9e9;
  }
  * { box-sizing: border-box; margin: 0; padding: 0; }
  html, body { width: 1200px; height: 1001px; overflow: hidden; background: var(--backdrop); }
  body { font-family: "Poppins", sans-serif; position: relative; }

  .flyer {
    position: absolute; left: 246px; top: 0; width: 707px; height: 1000px;
    background: var(--paper); transform: scale(0.94); transform-origin: 50% 50%;
    box-shadow: 0 10px 30px rgba(0,0,0,.18); overflow: hidden;
  }
  .hero-art { position: absolute; left: 0; top: 0; width: 707px; height: 600px; }

  .brand { position: absolute; right: 48px; top: 82px; text-align: center; }
  .brand-name { display: flex; align-items: center; gap: 8px; font-weight: 600; font-size: 40px; color: var(--red); letter-spacing: 1px; line-height: 1; }
  .brand-mark { width: 14px; height: 14px; background: var(--red); }
  .brand-by { display: flex; align-items: center; gap: 6px; margin-top: 6px; font-size: 15px; color: var(--grey); justify-content: center; }
  .brand-by::before, .brand-by::after { content: ""; width: 38px; height: 1.5px; background: var(--grey); }
  .brand-by b { font-weight: 600; }

  .headline {
    position: absolute; left: 60px; top: 216px; color: #fff; font-weight: 800;
    font-size: 44px; line-height: 46px; letter-spacing: -0.5px;
    text-shadow: 2px 3px 4px rgba(0,0,0,.55);
  }
  .intro { position: absolute; left: 65px; top: 413px; width: 350px; color: #fff; font-size: 14px; line-height: 18.5px; }

  .dots { position: absolute; left: 298px; top: 524px; display: grid; grid-template-columns: repeat(6, 4px); gap: 10px 13px; }
  .dots span { width: 4px; height: 4px; border-radius: 50%; background: var(--red); }

  .services { position: absolute; left: 52px; top: 572px; }
  .services h2 { color: var(--red); font-size: 28px; font-weight: 700; line-height: 36px; margin-bottom: 6px; }
  .services ul { list-style: none; }
  .services li { display: flex; align-items: center; gap: 11px; height: 29.4px; font-size: 14.5px; color: var(--ink); }
  .tick { width: 21px; height: 21px; background: var(--red); flex: none; }

  .more { position: absolute; left: 46px; top: 795px; color: var(--red); font-weight: 700; font-size: 13.5px; }
  .phone {
    position: absolute; left: 44px; top: 823px; width: 340px; height: 58px; background: var(--red);
    display: flex; align-items: center; justify-content: center; gap: 10px; color: #fff; font-weight: 700; font-size: 35px;
  }
  .contact { position: absolute; left: 52px; color: var(--grey); font-weight: 700; display: flex; align-items: center; gap: 10px; }
  .contact.email { top: 895px; font-size: 20px; }
  .contact.web { top: 926px; font-size: 26px; }

  .gallery-shot { position: absolute; left: 431px; width: 252px; }
  .shot-bath { top: 408px; height: 178px; background: linear-gradient(135deg, #8d8d8d, #c9c9c7 55%, #7a5a3e); clip-path: polygon(0 14%, 100% 0, 100% 100%, 0 100%); }
  .shot-kitchen { top: 597px; height: 180px; background: linear-gradient(160deg, #c08a57 0 30%, #f2f2f0 45%, #8c8782 100%); }
  .shot-dining { top: 790px; height: 163px; background: linear-gradient(180deg, #f4f4f4 0 35%, #3f4a4a 55%, #b07a45 100%); }
</style>
</head>
<body>
  <article class="flyer">
    <svg class="hero-art" viewBox="0 0 707 600" aria-hidden="false">
      <defs>
        <linearGradient id="heroTone" x1="0" y1="0" x2="1" y2="1">
          <stop offset="0" stop-color="#4f7fc9"/>
          <stop offset=".3" stop-color="#b9bcc0"/>
          <stop offset=".65" stop-color="#8e8f8c"/>
          <stop offset="1" stop-color="#7a5237"/>
        </linearGradient>
      </defs>
      <g role="img" aria-label="Photo of a renovated weatherboard home with a timber access ramp and deck">
        <polygon points="0,85 707,262 707,378 0,578" fill="url(#heroTone)"/>
      </g>
      <polygon points="157,108 707,250 707,272 157,128" fill="var(--red)"/>
      <polygon points="53,408 415,408 415,470 0,582 0,560 53,546" fill="var(--red)"/>
    </svg>

    <div class="brand">
      <div class="brand-name"><span class="brand-mark"></span>DWELLCRAFT</div>
      <div class="brand-by">by <b>ardent</b> constructions</div>
    </div>

    <h1 class="headline">Transform<br>your space<br>with high-quality<br>upgrades</h1>
    <p class="intro">We specialize in interior and exterior home renovations including new bathrooms, kitchens, balconies, decks, ramps, fireplaces, pergolas, verandahs, doorways, windows.</p>

    <div class="dots"><span></span><span></span><span></span><span></span><span></span><span></span><span></span><span></span><span></span><span></span><span></span><span></span></div>

    <div class="gallery-shot shot-bath" role="img" aria-label="Photo of a modern bathroom with freestanding bath and vanity"></div>
    <div class="gallery-shot shot-kitchen" role="img" aria-label="Photo of a renovated kitchen with timber cabinets and stone bench"></div>
    <div class="gallery-shot shot-dining" role="img" aria-label="Photo of an open-plan dining area with timber table"></div>

    <section class="services">
      <h2>Our Services</h2>
      <ul>
        <li><svg class="tick" viewBox="0 0 21 21"><rect width="21" height="21" fill="#c4070d"/><path d="M5 11l4 4 7-8" stroke="#fff" stroke-width="2.2" fill="none"/></svg>Bathroom &amp; Kitchen Renovations</li>
        <li><svg class="tick" viewBox="0 0 21 21"><rect width="21" height="21" fill="#c4070d"/><path d="M5 11l4 4 7-8" stroke="#fff" stroke-width="2.2" fill="none"/></svg>Home Extensions &amp; Full Home Renovations</li>
        <li><svg class="tick" viewBox="0 0 21 21"><rect width="21" height="21" fill="#c4070d"/><path d="M5 11l4 4 7-8" stroke="#fff" stroke-width="2.2" fill="none"/></svg>Ramps &amp; Accessibility Modifications</li>
        <li><svg class="tick" viewBox="0 0 21 21"><rect width="21" height="21" fill="#c4070d"/><path d="M5 11l4 4 7-8" stroke="#fff" stroke-width="2.2" fill="none"/></svg>Decks, Verandahs, Balconies</li>
        <li><svg class="tick" viewBox="0 0 21 21"><rect width="21" height="21" fill="#c4070d"/><path d="M5 11l4 4 7-8" stroke="#fff" stroke-width="2.2" fill="none"/></svg>Doorways, Windows &amp; Structural Upgrades</li>
        <li><svg class="tick" viewBox="0 0 21 21"><rect width="21" height="21" fill="#c4070d"/><path d="M5 11l4 4 7-8" stroke="#fff" stroke-width="2.2" fill="none"/></svg>Design &amp; Build Solutions</li>
      </ul>
    </section>

    <p class="more">MORE INFO:</p>
    <div class="phone">
      <svg width="18" height="18" viewBox="0 0 24 24"><path d="M6.6 10.8a15 15 0 0 0 6.6 6.6l2.2-2.2c.3-.3.7-.4 1-.2 1.1.4 2.3.6 3.6.6.6 0 1 .4 1 1V20c0 .6-.4 1-1 1A17 17 0 0 1 3 4c0-.6.4-1 1-1h3.5c.6 0 1 .4 1 1 0 1.3.2 2.5.6 3.6.1.3 0 .7-.2 1z" fill="#fff"/></svg>
      (03) 9012-4457
    </div>
    <p class="contact email">
      <svg width="20" height="14" viewBox="0 0 20 14"><rect width="20" height="14" fill="#c4070d"/><path d="M0 0l10 8 10-8" stroke="#fff" stroke-width="1.6" fill="none"/></svg>
      INFO@DWELLCRAFT.COM.AU
    </p>
    <p class="contact web">
      <svg width="20" height="20" viewBox="0 0 20 20" fill="none" stroke="#c4070d" stroke-width="1.6"><circle cx="10" cy="10" r="8.5"/><ellipse cx="10" cy="10" rx="3.8" ry="8.5"/><path d="M1.5 10h17M3 5.5h14M3 14.5h14"/></svg>
      DWELLCRAFT.COM.AU
    </p>
  </article>
</body>
</html>
```